Web Design For Coral Basin Pool Service

We are working with a company that wants a website for their pool service. Some sites to use for content/competitors and inspiration:
https://sacramento.lumawaterworks.example/builder/newbuild/repair/ppc
https://orchardsplashcareplus.example/
https://bluefinaquacare.example/
https://www.halvorsenplasterworks.example/pool-renovation-ga/
Thank you for taking the time to consider designing a website for us. We are web developers based in Stockton, CA, USA. Most of our projects go through the same process. Understanding this process may help you win a project with us. We custom-code all of our websites in-house. We don’t have any requirements as to what tools you use for your design, but we prefer Figma files. For any design that we label as four-stars, we send it to the client for review. The client picks the final design they want us to use. Once we complete this process, we will continue to show additional clients all the four-star sites and purchase them later. Your designs will have multiple chances to sell. For better chances of success, we ask that you follow these guidelines.
IMAGES:
If you use any images or icons in the design, we ask that you have a link to the asset so we can purchase the image/icon. Most of the designs we submit do not have the customer’s images on them unless they have some great images. Be creative; show us the feeling you are trying to portray with your image choices. Use any royalty-free site you choose. We subscribe to Adobe and mainly use their images, but we can purchase images outside of Adobe. PLEASE NOTE: we will not submit designs to clients with watermarks on the images.
FONTS:
We ask that you identify the fonts used in the design. This can be done in a message if you want. We typically use Google Fonts and Adobe Fonts.
CONTENT:
We're always open to different content and ideas. We often submit designs with stock images so the client can see our vision. We typically take pictures after the website launch to use their images with our vision. Lorem Ipsum is fine for paragraphs, but we ask that you write the headers in correct English. We want to be able to show the vision and identify the sections of the website.
INSPIRATION:
We typically add a couple of links in the brief of websites we like to help you get started in your design.
REVISIONS:
We do not often ask for revisions of the designs unless we see something in the design that may not appeal to the client. If there are slight changes that we want to make, we do that in the development process.
FEEDBACK:
We rarely give feedback on designs during the design process. We are working on many website projects and do not have the time to provide feedback. We usually respond if your request is well thought out and asks specific questions, but a note asking “feedback, please” usually goes unanswered.

```html
<!DOCTYPE html>
<html lang="en">
<head>
<meta charset="utf-8">
<title>Coral Basin Pool Service</title>
<link rel="stylesheet" href="https://fonts.googleapis.com/css2?family=Cinzel:wght@500;600&family=Poppins:wght@400;500;600&display=swap">
<style>
:root{
  --blue:#0b4fb0;
  --blue-dark:#083f8f;
  --sky:#2aa6f0;
  --ink:#1e2a3a;
  --muted:#6b7380;
  --line:#d6dbe3;
  --pale:#eaf2fb;
  --footer:#262626;
  --white:#fff;
}
*{box-sizing:border-box;margin:0;padding:0}
html,body{width:1200px;height:4601px;overflow:hidden;background:var(--white)}
body{font-family:"Poppins",sans-serif;color:var(--ink)}
.page{position:relative;width:1200px;height:4601px;overflow:hidden}
.abs{position:absolute}
.serif{font-family:"Cinzel",serif;font-weight:600;letter-spacing:1px}
.btn{position:absolute;display:flex;align-items:center;justify-content:center;font-size:10px;font-weight:600;letter-spacing:.5px;text-transform:uppercase}
.btn-solid{background:var(--sky);color:var(--white)}
.btn-line{border:1.5px solid var(--blue);color:var(--blue);background:var(--white)}
.btn-line-white{border:1.5px solid var(--white);color:var(--white)}
.photo{position:absolute}

/* header */
.brand{left:112px;top:14px;display:flex;align-items:center;gap:10px;color:var(--blue);font-family:"Cinzel",serif;font-weight:600;font-size:17px;line-height:1.05}
.brand-dot{width:22px;height:22px;border-radius:50%;background:var(--sky)}
.contact{top:24px;display:flex;align-items:center;gap:8px;font-size:11px;color:var(--muted);text-transform:uppercase}
.contact b{color:var(--sky);font-weight:500;text-transform:none}
.nav{left:0;top:68px;width:1200px;height:30px;background:var(--blue);display:flex;justify-content:center;align-items:center;gap:30px;font-size:10px;color:var(--white);text-transform:uppercase;letter-spacing:.5px}

/* hero */
.hero{left:0;top:98px;width:1200px;height:524px;background:linear-gradient(180deg,#8ec9ea 0%,#5fb2e2 35%,#3b98d6 70%,#1f7fc9 100%)}
.hero h1{position:absolute;left:0;width:1200px;top:322px;text-align:center;color:var(--white);font-family:"Cinzel",serif;font-weight:500;font-size:50px;letter-spacing:2px}
.hero p{position:absolute;left:0;width:1200px;top:392px;text-align:center;color:var(--white);font-size:17px;letter-spacing:.5px}

/* services */
.section-title{position:absolute;left:0;width:1200px;text-align:center;color:var(--blue);font-family:"Cinzel",serif;font-weight:600;font-size:34px;line-height:1.12;letter-spacing:1.5px}
.card{position:absolute;top:777px;width:228px;height:209px;border:1.5px solid var(--line);text-align:center;padding-top:18px}
.card svg{width:62px;height:62px}
.card h3{font-family:"Cinzel",serif;color:var(--blue);font-weight:600;font-size:14px;margin-top:10px;letter-spacing:.5px}
.card p{font-size:10px;color:var(--muted);line-height:1.5;padding:4px 22px 0}
.card a{display:block;font-size:9px;color:var(--sky);text-decoration:underline;margin-top:8px;text-transform:uppercase}

/* about */
.about{left:491px;top:1048px;width:709px;height:486px;background:var(--blue)}
.about h2{position:absolute;left:120px;top:104px;color:var(--white);font-family:"Cinzel",serif;font-weight:500;font-size:34px;line-height:1.1;letter-spacing:1px}
.about .kicker{position:absolute;left:118px;top:192px;color:var(--white);font-size:13px;text-transform:uppercase}
.about .body{position:absolute;left:118px;top:220px;width:470px;color:var(--white);font-size:12.5px;line-height:1.65}

/* how */
.how h2{position:absolute;left:116px;top:1640px;color:var(--blue);font-family:"Cinzel",serif;font-weight:600;font-size:32px;letter-spacing:1.5px}
.step{position:absolute;left:112px;display:flex;align-items:flex-start;gap:14px;font-family:"Cinzel",serif;font-size:14.5px;font-weight:500;color:var(--ink);line-height:1.2;width:440px}
.step .num{flex:none;width:38px;height:38px;border-radius:50%;border:1.5px solid var(--ink);display:flex;align-items:center;justify-content:center;font-size:17px}
.step .num.on{background:var(--sky);border-color:var(--sky);color:var(--white)}
.step span.t{padding-top:9px}
.how-photo{left:646px;top:1595px;width:554px;height:486px;background:linear-gradient(180deg,#9ab0cf 0%,#d9dde6 40%,#6e8fc2 65%,#2f5fad 100%)}
.how-caption{position:absolute;left:676px;top:1885px;width:440px;color:var(--white)}
.how-caption .row{display:flex;align-items:center;gap:12px;font-family:"Cinzel",serif;font-size:19px;letter-spacing:.5px}
.how-caption .row i{font-style:normal;width:34px;height:34px;border:1.5px solid var(--white);border-radius:50%;display:flex;align-items:center;justify-content:center;font-size:15px}
.how-caption p{font-size:12px;line-height:1.6;margin:6px 0 0 46px}

/* why */
.why-photo{left:0;top:2143px;width:553px;height:486px;background:linear-gradient(180deg,#123628 0%,#1d4a53 40%,#1c6ea8 75%,#0d4f93 100%)}
.why-caption{position:absolute;left:110px;top:2428px;width:400px;color:var(--white);text-align:right}
.why-caption h4{font-family:"Cinzel",serif;font-weight:500;font-size:20px;letter-spacing:.5px}
.why-caption p{font-size:12px;line-height:1.65;margin-top:6px}
.why h2{position:absolute;left:612px;top:2172px;color:var(--blue);font-family:"Cinzel",serif;font-weight:600;font-size:32px;letter-spacing:1.5px}
.tile{position:absolute;width:220px;height:126px;border:1.5px solid var(--line);text-align:center;padding-top:18px;font-family:"Cinzel",serif;font-size:12.5px;font-weight:500;color:var(--blue);letter-spacing:.3px}
.tile svg{width:52px;height:52px;display:block;margin:0 auto 14px}
.tile.on{background:var(--blue);border-color:var(--blue);color:var(--white)}

/* splash */
.splash{left:0;top:2691px;width:709px;height:486px;background:var(--pale)}
.splash h2{position:absolute;left:114px;top:130px;color:var(--blue);font-family:"Cinzel",serif;font-weight:600;font-size:34px;line-height:1.1;letter-spacing:1.5px}
.splash .name{position:absolute;left:112px;top:222px;font-size:13px}
.splash .body{position:absolute;left:112px;top:255px;width:470px;font-size:12px;line-height:1.65;color:var(--muted)}
.splash-photo{left:709px;top:2691px;width:491px;height:486px;background:linear-gradient(160deg,#c9a56a 0%,#7e9b52 30%,#47b7d4 60%,#1c8fc7 100%)}

/* projects */
.proj{position:absolute;width:300px}

/* subscribe */
.subscribe{left:0;top:4049px;width:1200px;height:259px;background:linear-gradient(180deg,#0d55b8,#0a49a3)}
.subscribe h2{position:absolute;left:0;width:1200px;top:120px;text-align:center;color:var(--white);font-family:"Cinzel",serif;font-weight:500;font-size:32px;letter-spacing:1.5px}
.field{position:absolute;left:329px;top:212px;width:364px;height:44px;border:1.5px solid #9cb8e3;color:#c8d8f1;font-size:10px;display:flex;align-items:center;padding-left:14px}

/* footer */
.footer{left:0;top:4308px;width:1200px;height:293px;background:var(--footer)}
.foot-brand{position:absolute;left:112px;top:112px;display:flex;align-items:center;gap:10px;color:var(--white);font-family:"Cinzel",serif;font-size:20px;font-weight:600;line-height:1.05}
.foot-links{position:absolute;left:411px;top:60px;color:var(--white);font-size:11px;line-height:21.5px}
.foot-contact{position:absolute;left:573px;display:flex;align-items:center;gap:8px;color:var(--white);font-size:11px;text-transform:uppercase}
.foot-contact b{color:var(--sky);font-weight:500;text-transform:none}
.social{width:11px;height:11px;border-radius:50%;background:var(--sky);display:inline-block}
.map{left:976px;top:4395px;width:112px;height:90px;background:linear-gradient(135deg,#cfe9d6,#a9d6c6 60%,#bcd8e8)}
.copy{position:absolute;left:0;top:4549px;width:1200px;height:52px;border-top:1px solid #3a3a3a;display:flex;align-items:center;justify-content:center;color:var(--white);font-size:11px;background:var(--footer)}
</style>
</head>
<body>
<div class="page">

  <!-- header -->
  <div class="abs brand"><span class="brand-dot"></span><span>Coral Basin<br>Pool Service</span></div>
  <div class="abs contact" style="left:327px">
    <svg width="20" height="14" viewBox="0 0 20 14"><rect x="1" y="1" width="18" height="12" fill="none" stroke="#0b4fb0" stroke-width="1.6"/><path d="M1 1l9 7 9-7" fill="none" stroke="#0b4fb0" stroke-width="1.6"/></svg>
    Email address: <b>hello@coralbasin.example</b>
  </div>
  <div class="abs contact" style="left:600px">
    <svg width="16" height="16" viewBox="0 0 24 24"><path d="M6.6 10.8a15 15 0 006.6 6.6l2.2-2.2a1 1 0 011-.25 11 11 0 003.6.6 1 1 0 011 1V20a1 1 0 01-1 1A17 17 0 013 4a1 1 0 011-1h3.5a1 1 0 011 1 11 11 0 00.6 3.6 1 1 0 01-.25 1z" fill="#0b4fb0"/></svg>
    Call &amp; discuss your pool needs: <b>(555) 014-2270</b>
  </div>
  <div class="btn btn-line" style="left:954px;top:16px;width:134px;height:38px">Request Service</div>

  <nav class="abs nav">
    <span>About Us</span><span>FAQ</span><span>Pool Services</span><span>Reviews</span><span>Pricing</span><span>Contact</span>
    <svg width="12" height="12" viewBox="0 0 12 12"><circle cx="5" cy="5" r="3.8" fill="none" stroke="#fff" stroke-width="1.3"/><path d="M8 8l3 3" stroke="#fff" stroke-width="1.3"/></svg>
  </nav>

  <!-- hero -->
  <div class="photo hero" role="img" aria-label="Wooden pool deck with white loungers beside a calm blue pool and the sea">
    <h1>Pool Perfection, Every Time</h1>
    <p>CLEAR WATER, CLEAR CONSCIENCE.</p>
    <div class="btn btn-line-white" style="left:534px;top:436px;width:132px;height:36px">Request Service</div>
  </div>

  <!-- services -->
  <h2 class="section-title" style="top:676px">The High-Water Mark<br>for Pool Care</h2>

  <div class="card" style="left:112px">
    <svg viewBox="0 0 64 64" fill="none" stroke="#2aa6f0" stroke-width="2"><path d="M26 14l4 12 12 4-12 4-4 12-4-12-12-4 12-4z"/><path d="M46 6l2 6 6 2-6 2-2 6-2-6-6-2 6-2z"/><path d="M44 40l1.5 4.5 4.5 1.5-4.5 1.5L44 52l-1.5-4.5L38 46l4.5-1.5z"/></svg>
    <h3>Pool Cleaning</h3>
    <p>Jump into clean crystal-clear water with professional weekly pool cleaning services.</p>
    <a>Read More</a>
  </div>
  <div class="card" style="left:361px">
    <svg viewBox="0 0 64 64" fill="none" stroke="#2aa6f0" stroke-width="2"><circle cx="32" cy="32" r="12"/><path d="M32 6v8M32 50v8M6 32h8M50 32h8M13.6 13.6l5.6 5.6M44.8 44.8l5.6 5.6M13.6 50.4l5.6-5.6M44.8 19.2l5.6-5.6"/><circle cx="32" cy="32" r="20"/></svg>
    <h3>Pool Repairs</h3>
    <p>Maintain your pool and pool equipment with technical pool repair services.</p>
    <a>Read More</a>
  </div>
  <div class="card" style="left:610px">
    <svg viewBox="0 0 64 64" fill="none" stroke="#2aa6f0" stroke-width="2"><rect x="8" y="8" width="48" height="48"/><circle cx="32" cy="32" r="18"/><path d="M8 32h48M32 8v48"/></svg>
    <h3>Pool Remodeling</h3>
    <p>Transform your existing pool with professional retiling, pool deck repairs, resurfacing and more.</p>
    <a>Read More</a>
  </div>
  <div class="card" style="left:859px">
    <svg viewBox="0 0 64 64" fill="none" stroke="#2aa6f0" stroke-width="2"><circle cx="26" cy="36" r="9"/><circle cx="26" cy="36" r="16" stroke-dasharray="6 4"/><circle cx="46" cy="18" r="5"/><circle cx="46" cy="18" r="10" stroke-dasharray="4 3"/></svg>
    <h3>Pool Installation</h3>
    <p>Build the pool of your dreams. Rely on our inground pool construction services to enhance your yard.</p>
    <a>Read More</a>
  </div>

  <!-- about -->
  <div class="photo" style="left:0;top:1048px;width:491px;height:486px;background:linear-gradient(180deg,#b7c6d3 0%,#e6ecf1 30%,#6c8a74 50%,#2c6aa3 72%,#b98a5a 100%)" role="img" aria-label="Infinity pool with wooden loungers and a glass railing overlooking the sea"></div>
  <div class="abs about">
    <h2>About Coral Basin<br>Pool Service</h2>
    <div class="kicker">Providing pool services to America since 2002</div>
    <p class="body">Lorem ipsum dolor sit amet, consectetur adipiscing elit, sed do eiusmod tempor incididunt ut labore et dolore magna aliqua. Quis ipsum suspendisse ultrices gravida. Risus commodo viverra maecenas accumsan lacus vel facilisis.</p>
    <div class="btn btn-solid" style="left:118px;top:324px;width:132px;height:36px">Read More</div>
    <div class="btn btn-line-white" style="left:264px;top:324px;width:134px;height:36px">Request Service</div>
  </div>

  <!-- how it works -->
  <section class="how">
    <h2>How It Works</h2>
    <div class="step" style="top:1710px"><span class="num on">1</span><span class="t">Submit your service request</span></div>
    <div class="step" style="top:1777px"><span class="num">2</span><span class="t">We connect you with a certified service technician</span></div>
    <div class="step" style="top:1843px"><span class="num">3</span><span class="t">A service technician will reach out to you shortly</span></div>
    <div class="step" style="top:1910px"><span class="num">4</span><span class="t">Back to enjoying your backyard</span></div>
    <div class="btn btn-line" style="left:112px;top:1982px;width:134px;height:36px">Request Service</div>
    <div class="photo how-photo" role="img" aria-label="White villa with columns behind a backyard pool at dusk"></div>
    <div class="how-caption">
      <div class="row"><i>1</i>Submit Your Service Request</div>
      <p>It is very important to us that customers meet the owner, give the history of their pool, so that any kinks can be worked out before we start regular service. Pool Service cannot be quoted properly over the phone</p>
    </div>
  </section>

  <!-- why choose -->
  <section class="why">
    <div class="photo why-photo" role="img" aria-label="Lit pool with a stone wall and palms at night"></div>
    <div class="why-caption">
      <h4>Worry Free Guarantee</h4>
      <p>Forget about fluctuating water chemistry. In fact, forget about buying and lugging chemicals, troubleshooting problems, remembering to latch the gate, whether its safe to swim, or if your filter's making a funny noise</p>
    </div>
    <h2>Why Choose Us</h2>
    <div class="tile on" style="left:611px;top:2241px">
      <svg viewBox="0 0 52 52" fill="none" stroke="#fff" stroke-width="2"><circle cx="26" cy="24" r="16"/><circle cx="26" cy="24" r="11"/><path d="M20 24l4 4 8-8"/><path d="M18 38l-3 10 6-3 5 4M34 38l3 10-6-3"/></svg>
      Worry Free Guarantee
    </div>
    <div class="tile" style="left:850px;top:2241px">
      <svg viewBox="0 0 52 52" fill="none" stroke="#2aa6f0" stroke-width="2"><path d="M4 22l10-10 8 4 8-4 8 0 10 10"/><path d="M14 22l12 12 4-4M22 26l8 8 4-4M30 22l8 8"/><path d="M4 22l10 10"/></svg>
      No Contracts. Ever
    </div>
    <div class="tile" style="left:611px;top:2386px">
      <svg viewBox="0 0 52 52" fill="none" stroke="#2aa6f0" stroke-width="2"><circle cx="26" cy="26" r="20"/><path d="M26 14v12h10"/></svg>
      Show Up On Time
    </div>
    <div class="tile" style="left:850px;top:2386px">
      <svg viewBox="0 0 52 52" fill="none" stroke="#2aa6f0" stroke-width="2"><path d="M14 4v26M8 30h12l3 18H5z"/><rect x="30" y="26" width="16" height="22" rx="2"/><path d="M34 26v-6h8v6"/></svg>
      Total Clean Promise
    </div>
    <div class="btn btn-solid" style="left:611px;top:2545px;width:132px;height:34px">Learn More</div>
  </section>

  <!-- splash -->
  <div class="abs splash">
    <h2>We Make a Splash with<br>Our Customers</h2>
    <div class="name">Dana Morrow</div>
    <p class="body">Never hesitate when it comes to potential electrical problems. Electrical issues can quickly develop into major catastrophes.</p>
    <div class="btn btn-solid" style="left:112px;top:314px;width:108px;height:36px">View All</div>
  </div>
  <div class="photo splash-photo" role="img" aria-label="Sun loungers beside a clear turquoise pool with tropical plants"></div>

  <!-- projects -->
  <h2 class="section-title" style="top:3228px">Completed Projects</h2>
  <div class="proj" style="left:121px;top:3300px;height:383px;background:linear-gradient(180deg,#8cc3ea,#c9d9c4 45%,#2b78bf 75%,#9a6a45)" role="img" aria-label="Tropical house with a pool and wooden deck"></div>
  <div class="proj" style="left:121px;top:3708px;height:212px;background:linear-gradient(180deg,#5b7d4e,#3f96d6 55%,#a2614a)" role="img" aria-label="Rectangular pool with a ladder surrounded by trees"></div>
  <div class="proj" style="left:450px;top:3300px;height:213px;background:linear-gradient(180deg,#c7e2f4,#e8ecef 40%,#2a93d5 70%,#8e7b68)" role="img" aria-label="Modern white house beside a long blue pool"></div>
  <div class="proj" style="left:450px;top:3540px;height:380px;background:linear-gradient(180deg,#d8cfc3,#b49376 40%,#1d7fb4 70%,#0f3f6e)" role="img" aria-label="Mediterranean villa with a lit pool at dusk"></div>
  <div class="proj" style="left:779px;top:3300px;height:383px;background:linear-gradient(180deg,#79a55b,#d7d2c8 40%,#7fbcc0 70%,#5c8e72)" role="img" aria-label="Glass pavilion with a reflecting pool and greenery"></div>
  <div class="proj" style="left:779px;top:3708px;height:212px;background:linear-gradient(180deg,#3c6f4c,#2c8fd8 45%,#1d63b8 80%,#b9775e)" role="img" aria-label="Curved pool with a round spa and brick edge"></div>
  <div class="btn btn-solid" style="left:541px;top:3954px;width:118px;height:32px">Explore More</div>

  <!-- subscribe -->
  <div class="abs subscribe">
    <h2>Subscribe for Latest Updates</h2>
    <div class="field">Enter Email</div>
    <div class="btn btn-solid" style="left:702px;top:212px;width:168px;height:44px">Subscribe</div>
  </div>

  <!-- footer -->
  <footer class="abs footer">
    <div class="foot-brand"><span class="brand-dot"></span><span>Coral Basin<br>Pool Service</span></div>
    <div class="foot-links">About Us<br>FAQ<br>Pool Services<br>Reviews<br>Pricing<br>Contact</div>
  </footer>
  <div class="foot-contact" style="top:4368px">
    <svg width="20" height="14" viewBox="0 0 20 14"><rect x="1" y="1" width="18" height="12" fill="none" stroke="#2aa6f0" stroke-width="1.6"/><path d="M1 1l9 7 9-7" fill="none" stroke="#2aa6f0" stroke-width="1.6"/></svg>
    Email address: <b>hello@coralbasin.example</b>
  </div>
  <div class="foot-contact" style="top:4407px">
    <svg width="16" height="16" viewBox="0 0 24 24"><path d="M6.6 10.8a15 15 0 006.6 6.6l2.2-2.2a1 1 0 011-.25 11 11 0 003.6.6 1 1 0 011 1V20a1 1 0 01-1 1A17 17 0 013 4a1 1 0 011-1h3.5a1 1 0 011 1 11 11 0 00.6 3.6 1 1 0 01-.25 1z" fill="#2aa6f0"/></svg>
    Call &amp; discuss your pool needs: <b>(555) 014-2270</b>
  </div>
  <div class="foot-contact" style="top:4462px">Follow us: <span class="social"></span><span class="social"></span><span class="social"></span></div>
  <div class="abs" style="left:976px;top:4370px;color:#fff;font-size:10px;text-transform:uppercase">Our Location</div>
  <div class="photo map" role="img" aria-label="Small map showing the service location"></div>
  <div class="copy">Copyright © 2024. All rights reserved.</div>

</div>
</body>
</html>
```